Interior Decoration and Concept Store needs a webpage design

Sophisticated website for my business, name Fern Hollow. Fern Hollow is a design service and homewares store run by interior decorator Marion Tolley.

Marion's qualification and work experience as an interior decorator, is able to provide advice and recommendations for interior and exterior concepts, colour consultations, furniture, lighting, decor concepts and products are sourced for individual projects. A re-upholstery service is also provided.

Facebook icon.
Projects page.
Profile page.
Established 2009
Medial page

```html
<!DOCTYPE html>
<html lang="en">
<head>
<meta charset="utf-8">
<title>Fern Hollow — Interior &amp; exterior concepts</title>
<link rel="stylesheet" href="https://fonts.googleapis.com/css2?family=Questrial&display=swap">
<style>
  :root {
    --white: #ffffff;
    --ink: #111111;
    --soft-grey: #b9b9b9;
    --accent: #e9ef6a;
    --hero-dark: #1c1b1a;
    --deck-dark: #1a1a18;
    --bar: #ffffff;
  }
  * { margin: 0; padding: 0; box-sizing: border-box; }
  html, body { width: 1200px; height: 2250px; overflow: hidden; background: #000; }
  body { font-family: "Questrial", sans-serif; color: var(--white); }

  .page { position: relative; width: 1200px; height: 2250px; }

  /* Hero */
  .hero { position: absolute; left: 0; top: 0; width: 1200px; height: 750px; overflow: hidden; }
  .hero-photo {
    position: absolute; inset: 0;
    background:
      radial-gradient(ellipse 320px 260px at 330px 400px, rgba(30,85,85,0.55), transparent 70%),
      radial-gradient(ellipse 420px 160px at 900px 680px, rgba(70,75,70,0.5), transparent 70%),
      linear-gradient(180deg, #2a2927 0%, #232220 55%, #2b211b 72%, #1c1a18 100%);
  }
  .hero-brand {
    position: absolute; top: 92px; left: 0; width: 100%;
    text-align: center; font-size: 38px; letter-spacing: 3px; color: var(--white);
  }
  .hero-title {
    position: absolute; top: 330px; left: 0; width: 100%; text-align: center;
    font-weight: 400; line-height: 1;
  }
  .hero-title .line-one {
    display: block; font-size: 74px; color: var(--white); letter-spacing: 1px;
    text-shadow: 0 0 14px rgba(255,255,255,0.55);
  }
  .hero-title .line-two {
    display: block; margin-top: 6px; font-size: 80px; color: var(--soft-grey); letter-spacing: 3px;
  }

  .scroll-arrow { position: absolute; left: 540px; width: 120px; height: 30px; }
  .hero .scroll-arrow { top: 690px; }
  .about .scroll-arrow { top: 690px; }

  /* Navigation bar */
  .nav-bar {
    position: absolute; left: 0; width: 1200px; height: 62px; background: var(--bar);
    color: var(--ink);
  }
  .nav-brand {
    position: absolute; left: 27px; top: 17px; font-size: 24px; letter-spacing: 2px; color: var(--ink);
  }
  .nav-links { position: absolute; top: 22px; left: 0; list-style: none; }
  .nav-links li { position: absolute; font-size: 18px; white-space: nowrap; }
  .nav-links .about-link { left: 753px; }
  .nav-links .projects-link { left: 858px; }
  .nav-links .contact-link { left: 995px; }
  .social-mark {
    position: absolute; left: 1151px; top: 12px; width: 36px; height: 36px;
    background: var(--ink); border-radius: 4px;
  }

  /* About */
  .about { position: absolute; left: 0; top: 750px; width: 1200px; height: 750px; overflow: hidden; }
  .about .nav-bar { top: 0; }
  .about-photo {
    position: absolute; left: 0; top: 62px; width: 1200px; height: 688px;
    background:
      radial-gradient(ellipse 110px 90px at 665px 330px, rgba(120,60,140,0.55), transparent 75%),
      radial-gradient(ellipse 500px 300px at 600px 420px, rgba(70,70,68,0.45), transparent 75%),
      linear-gradient(180deg, #151a14 0%, #1c1f1a 35%, #2a2824 60%, #1f1b17 100%);
  }
  .about-lead {
    position: absolute; top: 175px; left: 0; width: 100%; text-align: center;
    font-size: 22px; color: var(--white);
  }
  .highlight { color: var(--accent); }
  .about-range {
    position: absolute; top: 284px; left: 80px; font-size: 16px; line-height: 22.5px;
  }
  .about-services {
    position: absolute; top: 449px; right: 68px; text-align: right; font-size: 16px; line-height: 22.5px;
  }
  .about-note {
    position: absolute; top: 619px; left: 0; width: 1380px; text-align: center;
    font-size: 16px; color: var(--accent);
  }

  /* Projects */
  .projects { position: absolute; left: 0; top: 1500px; width: 1200px; height: 750px; overflow: hidden; }
  .projects .nav-bar { top: 0; }
  .project-grid {
    position: absolute; left: 0; top: 62px; width: 1200px; height: 688px;
    display: grid; grid-template-columns: repeat(4, 300px); grid-template-rows: 229px 229px 230px;
  }
  .project-tile { position: relative; }
  .project-tile::after { content: ""; position: absolute; inset: 0; background: rgba(0,0,0,0.42); }
  .project-tile.is-active::after { background: transparent; }
  .tile-lounge { background: linear-gradient(160deg, #cfc8bd, #8d857a 60%, #5a544c); }
  .tile-beanbag { background: linear-gradient(180deg, #e7e4de, #bfbcb5 60%, #8b8a55); }
  .tile-kitchen { background: linear-gradient(160deg, #e4e4e2, #b9b7b3 70%, #7b5a3d); }
  .tile-console { background: linear-gradient(170deg, #d9d6cf, #9c8f80 65%, #6a5e52); }
  .tile-billiard { background: linear-gradient(170deg, #b8b2aa, #7b736a 60%, #3d3630); }
  .tile-gallery { background: linear-gradient(150deg, #f4f2ea 0%, #e8d36a 22%, #f3f1ec 45%, #d9d7d3 70%, #8a4b2a 100%); }
  .tile-study { background: linear-gradient(170deg, #d8d6d2, #a69a86 60%, #6e6352); }
  .tile-armchair { background: linear-gradient(170deg, #e2e0dc, #b4b0a6 60%, #6b6a3c); }
  .tile-terrace { background: linear-gradient(170deg, #cfd6d9, #a0a59f 55%, #7d6e54); }
  .tile-bath { background: linear-gradient(170deg, #1f2a3c, #4a5a72 55%, #dedfe0); }
  .tile-dining { background: linear-gradient(170deg, #b9aa92, #8c7657 60%, #5b4530); }
  .tile-breakfast { background: linear-gradient(170deg, #e6e4e0, #bdb3a2 60%, #8a7458); }
</style>
</head>
<body>
<main class="page">

  <section class="hero">
    <div class="hero-photo" role="img" aria-label="Dim living room with a teal chest of drawers, fireplace and patterned rug"></div>
    <div class="hero-brand">FERN HOLLOW</div>
    <h1 class="hero-title">
      <span class="line-one">Interior &amp; exterior</span>
      <span class="line-two">CONCEPTS</span>
    </h1>
    <svg class="scroll-arrow" viewBox="0 0 120 30" aria-hidden="true"><polygon points="0,0 120,0 60,30" fill="#ffffff"/></svg>
  </section>

  <section class="about">
    <header class="nav-bar">
      <div class="nav-brand">FERN HOLLOW</div>
      <ul class="nav-links">
        <li class="about-link">ABOUT</li>
        <li class="projects-link">PROJECTS</li>
        <li class="contact-link">CONTACT</li>
      </ul>
      <span class="social-mark" aria-label="Social page"></span>
    </header>
    <div class="about-photo" role="img" aria-label="Evening deck with white lounge chairs and a colourful cushion against bamboo"></div>
    <p class="about-lead">Fern Hollow is a design service and homewares store run by interior decorator <span class="highlight">Marion Tolley</span></p>
    <p class="about-range">
      Inspiration is drawn from passion for quality products...<br>
      the homewares range is stylish and consists of <span class="highlight">unique</span> furniture pieces, decor accessories and lighting,<br>
      There is an evolving product range...
    </p>
    <p class="about-services">
      Marion's qualification and work <span class="highlight">experience</span> as an interior decorator<br>
      means that she is able to provide advice and recommendations<br>
      for interior and exterior concepts, colour consultations, furniture, lighting,<br>
      decor concepts and products are sourced for individual projects.
    </p>
    <p class="about-note">A re-upholstery service is also provided</p>
    <svg class="scroll-arrow" viewBox="0 0 120 30" aria-hidden="true"><polygon points="0,0 120,0 60,30" fill="#ffffff"/></svg>
  </section>

  <section class="projects">
    <header class="nav-bar">
      <div class="nav-brand">FERN HOLLOW</div>
      <ul class="nav-links">
        <li class="about-link">ABOUT</li>
        <li class="projects-link">PROJECTS</li>
        <li class="contact-link">CONTACT</li>
      </ul>
      <span class="social-mark" aria-label="Social page"></span>
    </header>
    <div class="project-grid">
      <div class="project-tile tile-lounge" role="img" aria-label="Lounge with armchair and throw"></div>
      <div class="project-tile tile-beanbag" role="img" aria-label="White room with green beanbag"></div>
      <div class="project-tile tile-kitchen" role="img" aria-label="Kitchen with wall clock and orange vase"></div>
      <div class="project-tile tile-console" role="img" aria-label="Carved timber console table"></div>
      <div class="project-tile tile-billiard" role="img" aria-label="Living room with billiard table"></div>
      <div class="project-tile tile-gallery is-active" role="img" aria-label="Bright hallway with yellow artwork and bowl"></div>
      <div class="project-tile tile-study" role="img" aria-label="Study with timber shelving and desk"></div>
      <div class="project-tile tile-armchair" role="img" aria-label="Olive armchair in a white room"></div>
      <div class="project-tile tile-terrace" role="img" aria-label="Terrace with chairs and glass balustrade"></div>
      <div class="project-tile tile-bath" role="img" aria-label="Bathroom with navy tiles and white bath"></div>
      <div class="project-tile tile-dining" role="img" aria-label="Timber dining table and chairs"></div>
      <div class="project-tile tile-breakfast" role="img" aria-label="Breakfast nook with timber table"></div>
    </div>
  </section>

</main>
</body>
</html>
```